Something that stands out and has more of a modern look to it...will be printing on plastic cards so keep in mind and review old business card as reference

Industry/Entity Type

Real Estate Agent

Contact Information for Business Card

Front of business card will have picture and information the back of card can have logo or name in cursive etc

Logo Text

Marcus Belvane

Font styles to use
Decorative
Script

Colors

Designer to choose colors to be used in the design.

Requirements
Must have
• Must have "Harborline 47" logo and state "Quiet Summit Realty Inc Brokerage*" next to it.
• Offices in: Toronto, Markham, Durham
• *Independently Owned and Operated trademarks owned by Harborline 47 Real Estate LLC used under license or authorized sub-license. 2017 Harborline 47 Canada Limited Partnership. (See old business card for reference)
• Email address: marcus@mbelvanehomes.example
• Website: www.MBelvaneHomes.example
• Direct: 647-555-0143
• Name: Marcus Bel Vane
• Office: 905-555-0178
Nice to have
• Maybe a catchy slogan
• One side can have my name designed or the Logo
Should not have
• The Harborline 47 Logo too large or focused on (my business requires me just to have this somewhere on the card).
• Yellow and black theme

```html
<!DOCTYPE html>
<html lang="en">
<head>
<meta charset="utf-8">
<title>Marcus Bel Vane – Business Card</title>
<link rel="stylesheet" href="https://fonts.googleapis.com/css2?family=Cookie&family=Montserrat:wght@400;500;700&display=swap">
<style>
  :root {
    --sky: #00b6ee;
    --sky-deep: #1689d6;
    --paper: #ffffff;
    --paper-shade: #eef0f2;
    --ink: #3a3a3a;
    --ink-soft: #8a8a8a;
    --logo-ink: #3b3b3b;
    --backdrop: #e6e8eb;
    --script: "Cookie", cursive;
    --sans: "Montserrat", sans-serif;
  }
  * { box-sizing: border-box; margin: 0; padding: 0; }
  html, body { width: 1200px; height: 900px; overflow: hidden; }
  body {
    background: var(--backdrop);
    font-family: var(--sans);
    display: flex;
    flex-direction: column;
    align-items: center;
    justify-content: center;
    gap: 40px;
  }
  .card {
    position: relative;
    width: 640px;
    height: 366px;
    border-radius: 4px;
    overflow: hidden;
    box-shadow: 0 8px 24px rgba(0,0,0,0.18);
  }

  /* Back side */
  .card-back {
    background: linear-gradient(160deg, var(--sky) 0%, var(--sky-deep) 100%);
    display: flex;
    flex-direction: column;
    align-items: center;
    justify-content: center;
    color: var(--paper);
  }
  .card-back .signature {
    font-family: var(--script);
    font-size: 88px;
    line-height: 1;
    color: var(--paper-shade);
  }
  .card-back .slogan {
    margin-top: 10px;
    font-size: 17px;
    letter-spacing: 0.5px;
  }

  /* Front side */
  .card-front { background: linear-gradient(180deg, var(--paper) 55%, var(--paper-shade) 100%); }
  .brand-panel {
    position: absolute;
    inset: 0;
    width: 100%;
    height: 100%;
  }
  .brand-column {
    position: absolute;
    left: 0; top: 0;
    width: 270px;
    height: 100%;
    display: flex;
    flex-direction: column;
    align-items: center;
    padding-top: 34px;
  }
  .portrait {
    width: 150px;
    height: 150px;
    border-radius: 50%;
    border: 4px solid var(--paper-shade);
    background: radial-gradient(circle at 50% 40%, #7a6a60 0%, #3f4a5a 55%, #2c3f73 100%);
  }
  .brokerage {
    margin-top: 16px;
    text-align: center;
    color: var(--logo-ink);
  }
  .brokerage .brand-name {
    font-size: 22px;
    font-weight: 700;
    letter-spacing: -0.5px;
  }
  .brokerage .brand-office {
    font-size: 8px;
    font-weight: 500;
    text-transform: uppercase;
    letter-spacing: 0.6px;
    margin-top: 3px;
  }
  .legal {
    margin-top: 14px;
    width: 220px;
    font-size: 7.5px;
    line-height: 1.45;
    color: var(--paper);
    text-align: center;
  }
  .contact-column {
    position: absolute;
    left: 320px; top: 48px;
    right: 24px;
    color: var(--ink);
  }
  .contact-column .agent-name {
    font-family: var(--script);
    font-size: 58px;
    line-height: 0.9;
    color: var(--sky);
  }
  .contact-column .agent-role {
    font-size: 15px;
    color: var(--ink-soft);
    margin-bottom: 26px;
  }
  .contact-block { font-size: 15px; line-height: 1.4; margin-bottom: 20px; }
  .contact-line { display: flex; align-items: center; gap: 8px; font-size: 14.5px; line-height: 1.55; }
  .contact-line svg { width: 14px; height: 14px; flex: none; }
</style>
</head>
<body>

  <section class="card card-back" aria-label="Card back">
    <h1 class="signature">Marcus Bel Vane</h1>
    <p class="slogan">“First Class Award Winning Service!”</p>
  </section>

  <section class="card card-front" aria-label="Card front">
    <svg class="brand-panel" viewBox="0 0 640 366" preserveAspectRatio="none" aria-hidden="true">
      <defs>
        <linearGradient id="panelFill" x1="0" y1="0" x2="0" y2="1">
          <stop offset="0" stop-color="#00b6ee"/>
          <stop offset="1" stop-color="#1689d6"/>
        </linearGradient>
      </defs>
      <polygon points="0,0 255,0 310,366 0,366" fill="url(#panelFill)"/>
    </svg>

    <div class="brand-column">
      <div class="portrait" role="img" aria-label="Portrait photo of the agent"></div>
      <div class="brokerage">
        <div class="brand-name">Harborline 47</div>
        <div class="brand-office">Quiet Summit Realty Inc. Brokerage*</div>
      </div>
      <p class="legal">*Independently Owned and Operated trademarks owned by Harborline 47 Real Estate LLC used under license or authorized sub-license. 2017 Harborline 47 Canada Limited Partnership.</p>
    </div>

    <div class="contact-column">
      <h2 class="agent-name">Marcus Bel Vane</h2>
      <p class="agent-role">Sales Representative</p>
      <p class="contact-block">Offices in:<br>Toronto, Markham, Durham</p>
      <p class="contact-block">Office: 905-555-0178<br>Direct: 647-555-0143</p>
      <p class="contact-line">
        <svg viewBox="0 0 16 16" aria-hidden="true"><circle cx="8" cy="8" r="7" fill="#00b6ee"/><path d="M4 6h8M4 10h8M8 1c-3 4-3 10 0 14M8 1c3 4 3 10 0 14" stroke="#fff" stroke-width="1" fill="none"/></svg>
        www.MBelvaneHomes.example
      </p>
      <p class="contact-line">
        <svg viewBox="0 0 16 16" aria-hidden="true"><rect x="1" y="3" width="14" height="10" rx="1" fill="none" stroke="#00b6ee" stroke-width="1.5"/><path d="M1.5 3.5 8 9l6.5-5.5" fill="none" stroke="#00b6ee" stroke-width="1.5"/></svg>
        marcus@mbelvanehomes.example
      </p>
    </div>
  </section>

</body>
</html>
```